Oven Cleaning Business owner needs business card design

Hi there,
Would like for a business card to be designed for myself, the owner of a professional oven cleaning business on the Sunshine Coast.
Would like it to look sleek, and modern-ish. Bit creative is encouraged too.
Include following:
Name/title: Corin ter Haghe, Owner
Phone number: 1300 482 916
Email: info@hearthshinecrew.com.au
Website: www.hearthshinecrew.com.au

```html
<!DOCTYPE html>
<html lang="en">
<head>
<meta charset="utf-8">
<title>Hearthshine Crew – Business Card</title>
<link rel="stylesheet" href="https://fonts.googleapis.com/css2?family=Arimo:wght@400;700&display=swap">
<style>
  :root {
    --bg: #3a3a3a;
    --paper: #ffffff;
    --ink: #1c1c1c;
    --muted: #555555;
    --teal: #4fc3c8;
    --card-black: #141414;
    --pattern: #222222;
    --divider: #9fdde0;
  }
  * { margin: 0; padding: 0; box-sizing: border-box; }
  html, body {
    width: 1200px; height: 801px; overflow: hidden;
    background: var(--bg);
    font-family: "Arimo", Arial, sans-serif;
  }
  .stage {
    width: 1200px; height: 801px;
    display: flex; align-items: center; justify-content: center; gap: 40px;
  }
  .card {
    position: relative;
    width: 540px; height: 330px;
    border-bottom: 4px solid var(--teal);
    box-shadow: 0 10px 24px rgba(0,0,0,.35);
    overflow: hidden;
  }
  .card--front { background: var(--paper); }
  .card--back { background: var(--card-black); }

  .brand {
    display: flex; align-items: center; gap: 12px;
    font-weight: 700; letter-spacing: 1px; text-transform: uppercase;
  }
  .brand__dot { width: 30px; height: 30px; border-radius: 50%; background: var(--teal); flex: none; }
  .brand__name { font-size: 30px; line-height: 1; }

  .card--front .brand { position: absolute; left: 70px; top: 70px; }
  .card--front .brand__name { color: var(--ink); }

  .holder { position: absolute; left: 40px; bottom: 70px; text-align: right; width: 210px; }
  .holder__name { color: var(--teal); font-size: 19px; text-transform: uppercase; letter-spacing: .2px; }
  .holder__title { color: var(--muted); font-size: 13px; margin-top: 4px; }

  .divider { position: absolute; left: 268px; bottom: 58px; width: 1px; height: 76px; background: var(--divider); }

  .contacts { position: absolute; left: 286px; bottom: 62px; list-style: none; }
  .contacts li {
    display: flex; align-items: center; gap: 7px;
    font-size: 13px; color: var(--ink); line-height: 22px;
  }
  .contacts svg { width: 11px; height: 11px; fill: var(--teal); flex: none; }

  .pattern { position: absolute; inset: 0; background: linear-gradient(135deg, var(--card-black), var(--pattern) 60%, var(--card-black)); }
  .card--back .brand { position: absolute; right: 60px; bottom: 120px; }
  .card--back .brand__name { color: #ffffff; }
</style>
</head>
<body>
<main class="stage">
  <section class="card card--front" aria-label="Card front">
    <div class="brand">
      <span class="brand__dot"></span>
      <span class="brand__name">Hearthshine Crew</span>
    </div>
    <div class="holder">
      <p class="holder__name">Corin ter Haghe</p>
      <p class="holder__title">Owner</p>
    </div>
    <span class="divider"></span>
    <ul class="contacts">
      <li><svg viewBox="0 0 16 16"><path d="M3 1l3 3-1.5 2a9 9 0 0 0 5.5 5.5L12 10l3 3-2 2C7 15 1 9 1 3z"/></svg>1300 482 916</li>
      <li><svg viewBox="0 0 16 16"><path d="M1 3h14v10H1z M1 3l7 6 7-6" fill="none" stroke="#4fc3c8" stroke-width="2"/></svg>info@hearthshinecrew.com.au</li>
      <li><svg viewBox="0 0 16 16"><circle cx="8" cy="8" r="7"/></svg>www.hearthshinecrew.com.au</li>
    </ul>
  </section>

  <section class="card card--back" aria-label="Card back">
    <div class="pattern" role="img" aria-label="Faint tone-on-tone repeating brand pattern across the card back"></div>
    <div class="brand">
      <span class="brand__dot"></span>
      <span class="brand__name">Hearthshine Crew</span>
    </div>
  </section>
</main>
</body>
</html>
```